Brand Identity Stationary Package

Hello I'm looking for a full branding package for my Property Management Company. I have a logo but looking to have the following
Business Card
Email signature
Facebook cover photo
Letterhead (word.doc)
#10 Envelope
Pocket Folder - link to 9x12 pocket folder design specs https://www.plorafine.ca/marketing-materials/presentation-folders
would like everything to match and be brand identifiable. The company looks after residential properties/apartments and some commercial properties. Attached is a zip of the files.
For Business Card
Name: Gideon Falkner
Position: Operations Manager
Number: 1 (506) 384-2917
Email: Gideon@quarrytide.ca
Website: Quarrytide.ca
Property Management

```html
<!DOCTYPE html>
<html lang="en">
<head>
<meta charset="utf-8">
<title>Quarrytide Letterhead</title>
<link href="https://fonts.googleapis.com/css2?family=Montserrat:wght@400;500;700&display=swap" rel="stylesheet">
<style>
  :root {
    --brand-green: #84ac3a;
    --ink: #1d1d1d;
    --paper: #ffffff;
    --backdrop: #e8e8e8;
    --sig-tone: #d9d9d9;
    --wave-line: #111111;
  }
  * { margin: 0; padding: 0; box-sizing: border-box; }
  html, body {
    width: 1200px; height: 874px; overflow: hidden;
    background: var(--backdrop);
    font-family: "Montserrat", Arial, sans-serif;
    color: var(--ink);
  }
  .letterhead {
    position: absolute; left: 310px; top: 27px;
    width: 580px; height: 820px;
    background: var(--paper);
    box-shadow: 0 2px 10px rgba(0,0,0,0.12);
    overflow: hidden;
  }
  .brand {
    position: absolute; left: 24px; top: 50px;
    display: flex; align-items: center; gap: 10px;
  }
  .brand-mark { width: 14px; height: 14px; background: var(--brand-green); }
  .brand-name {
    font-size: 34px; font-weight: 700; color: var(--ink); letter-spacing: 0.5px; line-height: 1;
  }
  .contact {
    position: absolute; left: 430px; top: 30px;
    font-size: 8.5px; line-height: 1.35;
  }
  .contact-name { color: var(--brand-green); font-weight: 700; text-transform: uppercase; }
  .contact-role { margin-bottom: 8px; }
  .contact-line { display: flex; align-items: center; gap: 6px; margin-left: 10px; }
  .contact-line svg { width: 8px; height: 8px; fill: var(--brand-green); }
  .header-rule {
    position: absolute; left: 60px; top: 118px;
    width: 500px; height: 1.5px; background: var(--brand-green);
  }
  .recipient {
    position: absolute; left: 70px; top: 176px;
    font-size: 9.5px; line-height: 14px;
  }
  .body-copy {
    position: absolute; left: 78px; top: 246px; width: 432px;
    font-size: 8.8px; line-height: 13px;
  }
  .body-copy p { margin-bottom: 11px; }
  .sign-off {
    position: absolute; left: 78px; top: 690px;
    font-size: 11px;
  }
  .signature {
    display: block; margin-top: 6px; margin-left: 6px;
    width: 80px; height: 26px; border-radius: 13px;
    background: var(--sig-tone);
  }
  .footer-wave { position: absolute; left: 0; top: 0; width: 580px; height: 820px; }
</style>
</head>
<body>
  <main class="letterhead">
    <div class="brand">
      <span class="brand-mark"></span>
      <span class="brand-name">Quarrytide</span>
    </div>

    <div class="contact">
      <div class="contact-name">Gideon Falkner</div>
      <div class="contact-role">Operations Manager</div>
      <div class="contact-line">
        <svg viewBox="0 0 24 24" aria-hidden="true"><path d="M6.6 10.8a15 15 0 0 0 6.6 6.6l2.2-2.2c.3-.3.7-.4 1-.2 1.1.4 2.3.6 3.6.6.6 0 1 .4 1 1V20c0 .6-.4 1-1 1A17 17 0 0 1 3 4c0-.6.4-1 1-1h3.5c.6 0 1 .4 1 1 0 1.3.2 2.5.6 3.6.1.3 0 .7-.2 1z"/></svg>
        <span>1 (506) 384-2917</span>
      </div>
      <div class="contact-line">
        <svg viewBox="0 0 24 24" aria-hidden="true"><path d="M2 5h20v14H2zm2 2v.5l8 5 8-5V7z"/></svg>
        <span>Gideon@quarrytide.ca</span>
      </div>
      <div class="contact-line">
        <svg viewBox="0 0 24 24" aria-hidden="true"><circle cx="12" cy="12" r="10"/></svg>
        <span>Quarrytide.ca</span>
      </div>
    </div>

    <div class="header-rule"></div>

    <div class="recipient">
      <div>Mr/s</div>
      <div>First Name and Last Name</div>
      <div>Company Name</div>
      <div>Address</div>
    </div>

    <div class="body-copy">
      <p>Lorem ipsum dolor sit amet,consectetur adipiscing sed do eiusmod tempor incididunt laboreet dolore magna aliqua.Ut enim ad minim.veniam, quis nostrud exercitation ullamco laboris nisi ut aliquip exea commodo consequat.Lorem ipsum dolor sit amet,consectetur adipiscing sed do eiusmod tempor incididunt.labore et dolore magna aliqua. Ut enim</p>
      <p>Lorem ipsum dolor sit amet, consectetur adipiscing sed do eiusmod tempor incididunt labore et dolore magna aliqua. Ut enim ad minim veniam, quis nostrud exercitation ullamco laboris nisi ut aliquip exea commodo consequat.Duis aute irure dolor in reprehenderit in voluptate velit esse cillum irure dolor in reprehenderit in voluptate velit esse irure</p>
      <p>Lorem ipsum dolor sit amet, consectetur adipiscing sed do eiusmod tempor incididunt labore et dolore magna aliqua. consequat. Duis aute irure dolor in.reprehenderit in voluptate velit esse cillum dolore eu fugiat nulla pariatur. Excepteur sint occaecat cupidatat non proident, sunt in culpa qui officia deserunt mollit,</p>
      <p>Lorem ipsum dolor sit amet, consectetur adipiscing sed do eiusmod tempor incididunt labore et dolore magna aliqua. Ut enim Lorem ipsum dolor sit amet, consectetur adipiscing sed do eiusmod tempor incididunt labore et dolore magna aliqua. Ut enim Lorem ipsum aliqua.ipsum</p>
      <p>Lorem ipsum dolor sit amet, consectetur adipiscing sed do eiusmod tempor incididunt labore et dolore magna aliqua. Ut enim ad minim veniam, quis nostrud exercitation ullamco laboris nisi ut aliquip exea commodo consequat.Duis aute irure dolor in reprehenderit in voluptate velit esse cillum irure dolor in reprehenderit in voluptate velit esse irure</p>
      <p>Lorem ipsum dolor sit amet, consectetur adipiscing sed do eiusmod tempor incididunt labore et dolore magna aliqua. Ut enim ad minim veniam, quis nostrud exercitation ullamco laboris nisi ut aliquip exea commodo consequat.Duis aute irure dolor in reprehenderit in voluptate velit esse cillum irure dolor in reprehenderit in voluptate velit esse irure</p>
    </div>

    <div class="sign-off">
      <div>Regards</div>
      <span class="signature" role="img" aria-label="Handwritten signature"></span>
    </div>

    <svg class="footer-wave" viewBox="0 0 580 820" aria-hidden="true">
      <path d="M4 822 C90 802 200 762 325 720 C440 683 520 672 582 664"
            fill="none" stroke="var(--wave-line)" stroke-width="6"/>
      <path d="M28 820 C112 802 218 772 338 734 C452 699 526 690 580 684 L580 820 Z"
            fill="var(--brand-green)"/>
    </svg>
  </main>
</body>
</html>
```